GLS biz card

We need a business card design for our new company based in Los Angeles called "Gold Lantern Studios". We develop film and television projects. We work with investors, financiers, film production companies, film distribution and sales companies as well as studios. We would like to incorporate our logo (see attached) on a two-sided card. We need to include: name and title, address, phone, email and company website.

Target Market(s)

Business, financial and studio clients

Industry/Entity Type

Business

Contact Information for Business Card

Two-sided. We are thinking of the logo on one side and the information on the back. Please feel free to be creative! Thanks.

Requirements
Must have
• Please include the following text information, excluding the "CAPS CATEGORY:" and please allow the ability for us to change the name, title and email address for each company employee):
• NAME & TITLE:
• Peter Dunmore
• Managing Partner
• COMPANY NAME:
• GOLD LANTERN STUDIOS (please use existing logo)
• COMPANY ADDRESS:
• KVT Arts Park
• 2480 Wexley Boulevard
• Arts Hall, 4th Floor
• Manhattan Beach, CA 90266
• COMPANY PHONE NUMBER:
• 310-555-4206
• COMPANY WEBSITE ADDRESS:
• www.goldlanternstudioshouse.com
• EMAIL ADDRESS: (only one per card)
• frank@goldlanternstudioshouse.com
• tizzy@goldlanternstudioshouse.com
• peter@goldlanternstudioshouse.com

```html
<!DOCTYPE html>
<html lang="en">
<head>
<meta charset="utf-8">
<title>Gold Lantern Studios – Business Card</title>
<link rel="stylesheet" href="https://fonts.googleapis.com/css2?family=Michroma&family=Arimo:wght@400&display=swap">
<style>
  :root {
    --page-bg: #ece9e4;
    --card-bg: #050607;
    --brand-cyan: #2bb6e3;
    --text-cyan: #3cc3ec;
    --card-shadow: rgba(0, 0, 0, 0.35);
  }
  * { box-sizing: border-box; margin: 0; padding: 0; }
  html, body {
    width: 1200px;
    height: 900px;
    overflow: hidden;
    background: var(--page-bg);
  }
  .canvas {
    position: relative;
    width: 1200px;
    height: 900px;
    display: flex;
    justify-content: center;
    align-items: center;
    gap: 90px;
  }
  .card {
    position: relative;
    width: 340px;
    height: 595px;
    background: var(--card-bg);
    border-radius: 6px;
    box-shadow: 0 14px 30px var(--card-shadow);
    color: var(--text-cyan);
  }
  .brand {
    position: absolute;
    left: 0;
    right: 0;
    display: flex;
    flex-direction: column;
    align-items: center;
    gap: 24px;
  }
  .brand-dot {
    width: 88px;
    height: 88px;
    border-radius: 50%;
    background: var(--brand-cyan);
  }
  .brand-name {
    font-family: "Michroma", sans-serif;
    font-weight: 400;
    font-size: 21px;
    line-height: 1.35;
    letter-spacing: 1px;
    text-align: center;
    color: var(--brand-cyan);
  }
  .card--info .brand { top: 40px; }
  .card--logo .brand { top: 190px; }

  .person {
    position: absolute;
    left: 36px;
    top: 262px;
  }
  .person-name {
    font-family: "Michroma", sans-serif;
    font-size: 29px;
    line-height: 1.2;
    font-weight: 400;
  }
  .person-title {
    margin-top: 20px;
    font-family: "Arimo", sans-serif;
    font-size: 16px;
    letter-spacing: 1px;
  }
  .contact {
    position: absolute;
    left: 36px;
    right: 16px;
    bottom: 38px;
    font-family: "Arimo", sans-serif;
    font-style: normal;
    font-size: 13.5px;
    line-height: 1.4;
  }
</style>
</head>
<body>
<main class="canvas">
  <section class="card card--info" aria-label="Business card, information side">
    <div class="brand">
      <div class="brand-dot"></div>
      <p class="brand-name">GOLD LANTERN<br>STUDIOS</p>
    </div>
    <div class="person">
      <h1 class="person-name">Peter<br>Dunmore</h1>
      <p class="person-title">MANAGING PARTNER</p>
    </div>
    <address class="contact">
      KVT Arts Park<br>
      2480 Wexley Boulevard<br>
      Arts Hall, 4th Floor<br>
      Manhattan Beach, CA 90266<br>
      Phone: 310-555-4206<br>
      Email: peter@goldlanternstudioshouse.com<br>
      www.goldlanternstudioshouse.com
    </address>
  </section>

  <section class="card card--logo" aria-label="Business card, logo side">
    <div class="brand">
      <div class="brand-dot"></div>
      <p class="brand-name">GOLD LANTERN<br>STUDIOS</p>
    </div>
  </section>
</main>
</body>
</html>
```